Surface Protection company needs cards

We are a New Zealand company that will apply nanotechnology coatings on surfaces to prevent growth and spread of bacteria, viruses, mold etc with a sprayer. We deal with large corporates, airlines, hospitals and schools so we are after a new modern, simple and clean look that will have great visual impact.
We a company that is focused on prevention and protection.

Company name, Vela Shield

Subtext, Antimicrobial Surface Protection

Logo, VS

Target Market(s)

Hospitals, Transport agencies, Airlines, Corporate entities

Contact Information for Business Card

Company name, VelaShield
Logo, VS

Gareth Tolley
velashieldnz@postbox.example
+64219305562
www.velashield.example.nz

Requirements
Must have
• Simple clean look.
Nice to have
• We apply nano coatings so try and incorporate this into a theme somehow

```html
<!DOCTYPE html>
<html lang="en">
<head>
<meta charset="utf-8">
<title>Vela Shield — Business Cards</title>
<link rel="stylesheet" href="https://fonts.googleapis.com/css2?family=Montserrat:wght@400;700;800&display=swap">
<style>
  :root {
    --canvas-bg: #e9e9ea;
    --card-white: #f6f6f6;
    --card-black: #000000;
    --brand-blue: #0a9ae3;
    --ink: #111111;
    --ink-soft: #444444;
    --rule: #9a9a9a;
    --tagline-dark: #5a5a5a;
    --tagline-light: #4a4a4a;
  }
  * { box-sizing: border-box; margin: 0; padding: 0; }
  html, body { width: 1200px; height: 800px; overflow: hidden; }
  body {
    background: var(--canvas-bg);
    font-family: "Montserrat", Arial, sans-serif;
    position: relative;
  }
  .card {
    position: absolute;
    width: 490px;
    height: 280px;
    box-shadow: 0 10px 28px rgba(0,0,0,0.18);
  }
  .card--front { left: 90px; top: 260px; background: var(--card-white); }
  .card--back  { left: 620px; top: 260px; background: var(--card-black); }

  .holder { position: absolute; left: 38px; top: 44px; width: 170px; }
  .holder__name {
    font-size: 21px;
    font-weight: 400;
    color: var(--ink);
    padding-bottom: 10px;
    border-bottom: 1px solid var(--rule);
  }
  .holder__name strong { font-weight: 800; }

  .brand { position: absolute; }
  .brand__name {
    font-weight: 800;
    color: var(--brand-blue);
    letter-spacing: 0.5px;
    line-height: 1;
  }
  .brand__tagline {
    font-weight: 400;
    line-height: 1;
    margin-top: 6px;
    letter-spacing: 0.3px;
  }
  .card--front .brand { right: 36px; top: 50px; }
  .card--front .brand__name { font-size: 30px; }
  .card--front .brand__tagline { font-size: 11.5px; color: var(--tagline-light); }

  .card--back .brand {
    left: 0; right: 0; top: 50%;
    transform: translateY(-50%);
    text-align: center;
  }
  .card--back .brand__name { font-size: 38px; }
  .card--back .brand__tagline { font-size: 13px; color: var(--tagline-dark); margin-top: 8px; }

  .contacts {
    position: absolute;
    right: 36px;
    bottom: 40px;
    list-style: none;
  }
  .contacts__item {
    display: flex;
    align-items: center;
    justify-content: flex-end;
    gap: 10px;
    font-size: 12px;
    color: var(--ink-soft);
    height: 22px;
  }
  .contacts__icon {
    width: 16px; height: 16px;
    border-radius: 3px;
    background: var(--brand-blue);
    display: flex; align-items: center; justify-content: center;
  }
  .contacts__icon svg { width: 10px; height: 10px; }
</style>
</head>
<body>

  <section class="card card--front" aria-label="Business card front">
    <div class="holder">
      <p class="holder__name">Gareth <strong>Tolley</strong></p>
    </div>

    <div class="brand">
      <p class="brand__name">VELASHIELD</p>
      <p class="brand__tagline">Antimicrobial Surface Protection</p>
    </div>

    <ul class="contacts">
      <li class="contacts__item">+64219305562
        <span class="contacts__icon">
          <svg viewBox="0 0 10 10"><path d="M2.2 1 L3.8 1 L4.4 3 L3.4 3.8 Q4.4 5.8 6.2 6.6 L7 5.6 L9 6.2 L9 7.8 Q8.6 9 7.4 9 Q1 8.4 1 2.6 Q1 1.4 2.2 1 Z" fill="#fff"/></svg>
        </span>
      </li>
      <li class="contacts__item">velashieldnz@postbox.example
        <span class="contacts__icon">
          <svg viewBox="0 0 10 10"><rect x="1" y="2.2" width="8" height="5.6" fill="none" stroke="#fff" stroke-width="1"/><path d="M1 2.4 L5 5.4 L9 2.4" fill="none" stroke="#fff" stroke-width="1"/></svg>
        </span>
      </li>
      <li class="contacts__item">www.velashield.example.nz
        <span class="contacts__icon">
          <svg viewBox="0 0 10 10" fill="none" stroke="#fff" stroke-width="0.9"><circle cx="5" cy="5" r="3.8"/><ellipse cx="5" cy="5" rx="1.6" ry="3.8"/><path d="M1.2 5 H8.8"/></svg>
        </span>
      </li>
    </ul>
  </section>

  <section class="card card--back" aria-label="Business card back">
    <div class="brand">
      <p class="brand__name">VELASHIELD</p>
      <p class="brand__tagline">Antimicrobial Surface Protection</p>
    </div>
  </section>

</body>
</html>
```